Kestrel Path Business card

We are a company that owns 2 compliance software programs for TV, Radio and Cable industries as well as an online job board. We need a professional business card that incorproates all three logos.

```html
<!DOCTYPE html>
<html lang="en">
<head>
<meta charset="utf-8">
<title>Kestrel Path Business Card</title>
<link href="https://fonts.googleapis.com/css2?family=Roboto:wght@400;500;700;900&display=swap" rel="stylesheet">
<style>
  :root{
    --navy:#2b2a72;
    --red:#ee4424;
    --blue:#1f86d6;
    --grey:#8a8f98;
    --paper:#ffffff;
    --backdrop:#2a2b2f;
    --ink:#1f1f4d;
  }
  *{box-sizing:border-box;margin:0;padding:0}
  html,body{width:1200px;height:800px;overflow:hidden}
  body{background:var(--backdrop);font-family:"Roboto",Arial,sans-serif;position:relative}

  .card{position:absolute;width:540px;height:309px;background:var(--paper);overflow:hidden;
        box-shadow:0 14px 30px rgba(0,0,0,.45)}
  .card--front{left:40px;top:245px}
  .card--back{left:620px;top:245px}

  /* brand names (stand-ins for the three product marks) */
  .brand{display:flex;flex-direction:column;align-items:flex-start;line-height:1;flex:none}
  .brand__row{display:flex;align-items:center;gap:6px}
  .brand__name{font-weight:900;letter-spacing:-.3px;white-space:nowrap}
  .brand__line{display:block}
  .brand__tag{font-weight:500;text-transform:uppercase;letter-spacing:.6px;margin-top:4px;white-space:nowrap}
  .brand--air .brand__name{color:var(--navy)}
  .brand--air .brand__tag{color:var(--navy)}
  .brand--coax .brand__name{color:var(--red)}
  .brand--coax .brand__tag{color:var(--navy)}
  .brand--stage .brand__name{color:var(--blue)}
  .brand__square{width:12px;height:12px;background:var(--red);flex:none}
  .brand__circle{width:14px;height:14px;border-radius:50%;border:3px solid var(--blue);flex:none}

  /* front */
  .front__logos{position:absolute;left:0;right:0;top:128px;display:flex;align-items:center;justify-content:center;gap:16px}
  .front__logos .brand__name{font-size:19px}
  .front__logos .brand__tag{font-size:6.5px}
  .divider{width:1.5px;height:64px;background:var(--navy);flex:none}

  /* back */
  .back__band{position:absolute;left:0;top:0;bottom:0;width:14px;background:var(--navy)}
  .back__logos{position:absolute;left:14px;top:0;bottom:0;width:94px}
  .back__logos-inner{position:absolute;left:50%;top:50%;width:289px;height:80px;
        transform:translate(-50%,-50%) rotate(-90deg);
        display:flex;align-items:center;justify-content:center;gap:10px}
  .back__logos .brand__name{font-size:12px;line-height:1.05}
  .back__logos .brand__tag{font-size:4.8px;letter-spacing:.4px}
  .back__logos .brand__circle{width:11px;height:11px;border-width:2.5px}
  .back__logos .brand__row{gap:4px}
  .back__logos .divider{height:40px}
  .back__bar{position:absolute;left:108px;top:0;bottom:0;width:8px;
        background:linear-gradient(to bottom,var(--navy) 0 50%,var(--red) 50% 100%)}

  .back__rows{position:absolute;left:134px;right:24px;top:22px;bottom:22px;display:flex;flex-direction:column}
  .contact-row{flex:1;display:flex;align-items:center;justify-content:space-between;border-bottom:1.5px solid var(--navy)}
  .contact-row:last-child{border-bottom:none}
  .contact-list{list-style:none;display:flex;flex-direction:column;gap:3px}
  .contact-list li{display:flex;align-items:center;gap:6px;font-size:10.5px;color:var(--ink)}
  .icon{width:13px;height:13px;border-radius:50%;background:var(--red);display:flex;align-items:center;justify-content:center;flex:none}
  .icon svg{width:8px;height:8px;fill:none;stroke:#fff;stroke-width:2;stroke-linecap:round;stroke-linejoin:round}
  .address{font-style:normal;font-size:10.5px;line-height:1.3;color:var(--ink);text-align:left}
</style>
</head>
<body>

<svg width="0" height="0" style="position:absolute" aria-hidden="true">
  <defs>
    <symbol id="i-phone" viewBox="0 0 24 24"><path d="M5 3h4l2 5-3 2a11 11 0 0 0 6 6l2-3 5 2v4a2 2 0 0 1-2 2A17 17 0 0 1 3 5a2 2 0 0 1 2-2z"/></symbol>
    <symbol id="i-mail" viewBox="0 0 24 24"><rect x="3" y="5" width="18" height="14" rx="1"/><path d="M3 6l9 7 9-7"/></symbol>
    <symbol id="i-web" viewBox="0 0 24 24"><circle cx="12" cy="12" r="9"/><path d="M3 12h18M12 3c3 3 3 15 0 18M12 3c-3 3-3 15 0 18"/></symbol>
  </defs>
</svg>

<section class="card card--front" aria-label="Kestrel Path card front">
  <div class="front__logos">
    <div class="brand brand--air">
      <div class="brand__row"><span class="brand__name">Airwave Ledger</span><span class="brand__square"></span></div>
      <span class="brand__tag">Broadcast Compliance</span>
    </div>
    <span class="divider"></span>
    <div class="brand brand--coax">
      <div class="brand__row"><span class="brand__name">Coaxline Check</span></div>
      <span class="brand__tag">MVPD Compliance</span>
    </div>
    <span class="divider"></span>
    <div class="brand brand--stage">
      <div class="brand__row"><span class="brand__circle"></span><span class="brand__name">StageCrew Board</span></div>
    </div>
  </div>
</section>

<section class="card card--back" aria-label="Kestrel Path card back">
  <div class="back__band"></div>
  <div class="back__logos">
    <div class="back__logos-inner">
      <div class="brand brand--air">
        <span class="brand__name"><span class="brand__line">Airwave</span><span class="brand__line">Ledger</span></span>
        <span class="brand__tag">Broadcast Compliance</span>
      </div>
      <span class="divider"></span>
      <div class="brand brand--coax">
        <span class="brand__name"><span class="brand__line">Coaxline</span><span class="brand__line">Check</span></span>
        <span class="brand__tag">MVPD Compliance</span>
      </div>
      <span class="divider"></span>
      <div class="brand brand--stage">
        <div class="brand__row"><span class="brand__circle"></span><span class="brand__name"><span class="brand__line">StageCrew</span><span class="brand__line">Board</span></span></div>
      </div>
    </div>
  </div>
  <div class="back__bar"></div>

  <div class="back__rows">
    <div class="contact-row">
      <ul class="contact-list">
        <li><span class="icon"><svg><use href="#i-phone"/></svg></span>555.555.5555</li>
        <li><span class="icon"><svg><use href="#i-mail"/></svg></span>info@companygmail.com</li>
        <li><span class="icon"><svg><use href="#i-web"/></svg></span>www.companyweb.com</li>
      </ul>
      <address class="address">PO BOX 123<br>Street Address<br>2nd Lane, Arizona</address>
    </div>
    <div class="contact-row">
      <ul class="contact-list">
        <li><span class="icon"><svg><use href="#i-phone"/></svg></span>555.555.5555</li>
        <li><span class="icon"><svg><use href="#i-mail"/></svg></span>info@companygmail.com</li>
        <li><span class="icon"><svg><use href="#i-web"/></svg></span>www.companyweb.com</li>
      </ul>
      <address class="address">PO BOX 123<br>Street Address<br>2nd Lane, Arizona</address>
    </div>
    <div class="contact-row">
      <ul class="contact-list">
        <li><span class="icon"><svg><use href="#i-phone"/></svg></span>555.555.5555</li>
        <li><span class="icon"><svg><use href="#i-mail"/></svg></span>info@companygmail.com</li>
        <li><span class="icon"><svg><use href="#i-web"/></svg></span>www.companyweb.com</li>
      </ul>
      <address class="address">PO BOX 123<br>Street Address<br>2nd Lane, Arizona</address>
    </div>
  </div>
</section>

</body>
</html>
```